Designing a brochures for an educational counseling service provider

We would like a 4 sided design on a 11x8.5 paper, half folded. I have including a sample design we did to give you an idea of what we envision but we welcome creativity to make beautiful looking flyers. Text for the flier is included as well as our logo.
- The most important thing is capturing our audience/market. We will be handing these flies to schools, organizations and individual clients.

www.vormtaleducationalconsultants.com

Target Market(s)

We are targeting international students wanting to study in the U.S and Canada.

Industry/Entity Type

Education

Requirements
Must have
• - Clean and clear
• - Our logo should visible and well placed.
• - Could you the pictures of students, libraries and school buildings or you could use the pictures we already have.
Nice to have
• We would like this to match business cards.

```html
<!DOCTYPE html>
<html lang="en">
<head>
<meta charset="utf-8">
<title>Educational Consultants – About Us &amp; Services</title>
<link rel="stylesheet" href="https://fonts.googleapis.com/css2?family=Source+Sans+3:wght@400;600;700&display=swap">
<style>
  :root {
    --navy: #1f3142;
    --orange: #f47b20;
    --ink: #2a2a2a;
    --paper: #ffffff;
  }
  * { margin: 0; padding: 0; box-sizing: border-box; }
  html, body { width: 1200px; height: 927px; overflow: hidden; background: var(--paper); }
  body { font-family: "Source Sans 3", Arial, sans-serif; color: var(--ink); }
  .page { position: relative; width: 1200px; height: 927px; overflow: hidden; }

  .student-photo {
    position: absolute; left: 0; top: 0; width: 212px; height: 905px;
    background: linear-gradient(180deg, #d9cbb3 0%, #c9a77f 25%, #6b4530 50%, #e9e2d6 72%, #b79b78 100%);
  }
  .library-photo {
    position: absolute; left: 598px; top: 440px; width: 132px; height: 465px;
    background: linear-gradient(180deg, #d8dde0 0%, #aab6bc 40%, #e7e9ea 75%, #f4f4f4 100%);
  }
  .footer-band { position: absolute; left: 0; bottom: 0; width: 1200px; height: 22px; background: var(--navy); }

  .section-bar {
    position: absolute; left: 167px; width: 1007px; height: 35px;
    background: var(--navy); display: flex; align-items: center;
  }
  .section-bar svg { flex: none; }
  .section-bar h2 {
    color: #fff; font-weight: 700; font-size: 27px; letter-spacing: 0.5px; margin-left: 8px; line-height: 1;
  }
  .bar-about { top: 27px; }
  .bar-services { top: 251px; }

  .col { position: absolute; font-size: 15.6px; line-height: 19.6px; text-align: justify; }
  .col p { margin-bottom: 9px; }
  .col h3 { color: var(--orange); font-size: 19px; font-weight: 700; line-height: 20px; margin-top: 2px; }
  .col h3 + p { margin-top: 0; }
  .lead { font-weight: 700; }
  .package-title { font-weight: 700; margin-bottom: 3px !important; }
  .package { list-style: none; text-align: left; font-size: 17px; line-height: 21px; margin-bottom: 1px; }
  .package li { position: relative; padding-left: 23px; }
  .package li::before {
    content: ""; position: absolute; left: 5px; top: 8px; width: 6px; height: 6px; background: var(--orange);
  }

  .about-left { left: 212px; top: 71px; width: 370px; }
  .about-right { left: 750px; top: 71px; width: 424px; }
  .services-left { left: 212px; top: 296px; width: 370px; }
  .services-right { left: 750px; top: 296px; width: 424px; }
</style>
</head>
<body>
<div class="page">
  <div class="student-photo" role="img" aria-label="Photo of a smiling student holding a book"></div>

  <header class="section-bar bar-about">
    <svg width="56" height="35" viewBox="0 0 56 35" aria-hidden="true"><polygon points="0,0 44,0 56,17.5 44,35 0,35" fill="var(--orange)"/></svg>
    <h2>ABOUT US</h2>
  </header>

  <section class="col about-left">
    <p>Our mission is to make quality education accessible and affordable to the families we serve. Our services are designed with the child’s future in mind. Whether one is seeking an academic or non-academic environment, it is important to us that we set our clients up for success.</p>
    <p>We are a family-centered organization and our</p>
  </section>
  <section class="col about-right">
    <p>goals are the same as those of our clients; for their child to thrive and reach their goals and dreams. With over 10 years of experience in the business, we are aware of the financial obstacles created by the ever increasing cost in education. Our expert consultants work closely with families to map out their educational budget and find the best affordable and quality educational options.</p>
  </section>

  <header class="section-bar bar-services">
    <svg width="56" height="35" viewBox="0 0 56 35" aria-hidden="true"><polygon points="0,0 44,0 56,17.5 44,35 0,35" fill="var(--orange)"/></svg>
    <h2>SERVICES</h2>
  </header>

  <section class="col services-left">
    <p><span class="lead">Finding the right school</span> or program for your child is one of the most important decisions your family will make. The right choice will make a major impact on your child’s future.</p>
    <p class="package-title">Our package includes:</p>
    <ul class="package">
      <li>Intake interview</li>
      <li>Present range of options based on needs and goals of the family</li>
      <li>Interview coaching</li>
      <li>Assistance with application and essays</li>
      <li>Updates on student progress throughout their enrollment with the school,</li>
      <li>Advisement on financial documents and visa applications</li>
    </ul>
    <h3>Boarding schools:</h3>
    <p>Students who want the best out of their grade school experience are likely to choose boarding schools because they are proven to better prepare students for university. North American boarding schools provide a quality dynamic experience that will facilitate personal growth in independence, leadership, and confidence as well as provide the academic curriculum necessary to prepare students for university.</p>
    <h3>College admission:</h3>
    <p>As Educational Consultants, we specialize in col-</p>
  </section>

  <div class="library-photo" role="img" aria-label="Photo of a student walking between tall library bookshelves"></div>

  <section class="col services-right">
    <p>lege/university admissions and we understand how confusing, time-consuming, and stressful the application process can be. Our experienced counselors are here to answer your questions and guide you step by step. As Parents and students may have limited access to information on schools, may not know or understand the entire process as a whole, nor where/how to begin, our experts counselors have a solutions.</p>
    <p>Clients increase the odds of admissions with our comprehensive plan of action. We believe that regardless of a student’s level of involvement in extra-curricular activities or preparedness, they still possess something they can offer to the university; therefore we help them shine on their college applications.</p>
    <h3>Transfer students:</h3>
    <p>Need to find a school an alternative school that is a better match for you? We work with students and families to transfer from one school to another.</p>
    <h3>Scholarships:</h3>
    <p>Funding the education for your children in some of the world’s top schools can be very expensive as tuition and fees increase at an average of 4% every year. We work with you to determine the budget for your family, applying to scholarship available and guide you through the financial aid process.</p>
    <p>Over 70% of our clients have been awarded scholarships or Financial Aid, making your education goals attainable an affordable, and your children education possible.</p>
  </section>

  <div class="footer-band"></div>
</div>
</body>
</html>
```